Power Point Template for Unique Indoor Advertising Company.

We need PowerPoint slide templates for our Sales Media Kit at our re-branded company based in Canada called "Bellwether Ad Collective".

Looking for a look that clearly and powerfully portrays our unique and effective indoor advertising billboards in our network.

Our Prime Billboards are strategically placed in high traffic areas of restaurants, pubs, nightclubs, fitness clubs, colleges and universities, and sports arenas.

Key features of our media is a captive audience and 100% gender specific.

You can visit our current website for info on our media (foxglovepromotions.ca)

Our Media Kits go out to small, medium business owners and advertising agenices and need to be eye-catching, trendy and slick.

Our logos are attached.

Deliverables are:

1) Presentation cover slide with rich graphic content and space for content.
2) Presentation body slide with room for content, 3-4 photos. This slide should have the following:
a) No graphic in the text area
b) Space for page number at the bottom.
3) Photoshop (PSD) files for all graphic elements.
4) Font files for all fonts used.

Target Market(s)

Advertising Agencies and Media Buyers

Industry/Entity Type

It Company

Font styles to use
Serif

Requirements
Must have
• Captivating and sleek look that is eye-catching and targeted.

```html
<!DOCTYPE html>
<html lang="en">
<head>
<meta charset="utf-8">
<title>Bellwether Ad Collective – Team &amp; Contact</title>
<link href="https://fonts.googleapis.com/css2?family=Arimo:wght@400;700&display=swap" rel="stylesheet">
<style>
  :root {
    --band-blue: #4455ff;
    --slide-bg: #f8f9fe;
    --ink-dark: #3d4f6b;
    --ink-soft: #6f737a;
    --ink-faint: #d3d8e1;
    --ring-navy: #1b4f7e;
    --teal: #34c9a0;
    --social-blue: #1a74c4;
    --social-slate: #3f4d63;
    --social-green: #3fd18f;
    --brand-red: #b3202a;
    --white: #ffffff;
    --panel-glass: rgba(255,255,255,0.17);
  }
  * { box-sizing: border-box; margin: 0; padding: 0; }
  html, body { width: 973px; height: 1200px; overflow: hidden; }
  body { background: var(--band-blue); font-family: "Arimo", Arial, sans-serif; position: relative; }

  .slide { position: absolute; left: 0; width: 973px; height: 530px; overflow: hidden; }
  .slide--team { top: 28px; background: var(--slide-bg); }
  .slide--contact { top: 600px; }

  .team__title { position: absolute; top: 20px; width: 100%; text-align: center; font-size: 42px; font-weight: 700; letter-spacing: 2px; color: var(--ink-dark); }
  .team__subtitle { position: absolute; top: 67px; width: 100%; text-align: center; font-size: 20px; font-weight: 700; letter-spacing: 0.5px; color: var(--ink-faint); }
  .page-number { position: absolute; left: 924px; top: 42px; width: 28px; height: 28px; border-radius: 50%; background: var(--teal); color: var(--white); font-size: 10px; text-align: center; line-height: 28px; }

  .member { position: absolute; top: 138px; width: 200px; margin-left: -100px; text-align: center; }
  .member__portrait { width: 160px; height: 140px; margin: 0 auto; border-radius: 50%; border: 3px solid var(--ring-navy); background: linear-gradient(180deg, #ffffff 0%, #e9ecf2 55%, #2a2f38 56%, #121418 100%); }
  .member__name { margin-top: 28px; font-size: 21px; font-weight: 700; color: var(--ink-dark); }
  .member__role { margin-top: 9px; font-size: 16px; color: var(--ink-soft); }
  .member__social { margin-top: 40px; display: flex; justify-content: center; gap: 2px; }
  .member__social span { width: 28px; height: 28px; border-radius: 50%; display: block; }
  .social--a { background: var(--social-blue); }
  .social--b { background: var(--social-slate); }
  .social--c { background: var(--social-green); }

  .brand { position: absolute; left: 50px; top: 487px; display: flex; align-items: center; gap: 6px; font-size: 16px; font-weight: 700; color: var(--ink-dark); }
  .brand__dot { width: 14px; height: 14px; border-radius: 50%; background: var(--brand-red); }
  .domain { position: absolute; right: 47px; top: 494px; font-size: 11px; font-weight: 700; letter-spacing: 1.5px; color: var(--ink-faint); }

  .city-backdrop { position: absolute; inset: 0; background: linear-gradient(180deg, #4f86cc 0%, #4a80c4 28%, #3d6fa8 50%, #3a6a9c 70%, #355f8a 100%); }
  .contact__title { position: absolute; top: 48px; width: 100%; text-align: center; font-size: 32px; font-weight: 700; color: var(--white); }

  .contact-item { position: absolute; color: var(--white); }
  .contact-item__icon { position: absolute; }
  .contact-item__label { position: absolute; font-size: 17px; font-weight: 700; text-decoration: underline; white-space: nowrap; }
  .contact-item__panel { position: absolute; background: var(--panel-glass); padding: 2px 4px; font-size: 17px; line-height: 1.5; white-space: nowrap; }
  .panel--tight { line-height: 1.2; font-size: 16px; }
</style>
</head>
<body>

<section class="slide slide--team">
  <h1 class="team__title">OUR TEAM</h1>
  <p class="team__subtitle">YOUR GREAT SUBTITLE</p>
  <div class="page-number">7</div>

  <div class="member" style="left:186px">
    <div class="member__portrait" role="img" aria-label="Team member portrait placeholder"></div>
    <p class="member__name">John DOE</p><p class="member__role">Title</p>
    <div class="member__social"><span class="social--a"></span><span class="social--b"></span><span class="social--c"></span></div>
  </div>
  <div class="member" style="left:389px">
    <div class="member__portrait" role="img" aria-label="Team member portrait placeholder"></div>
    <p class="member__name">Paula KO</p><p class="member__role">Title</p>
    <div class="member__social"><span class="social--a"></span><span class="social--b"></span><span class="social--c"></span></div>
  </div>
  <div class="member" style="left:599px">
    <div class="member__portrait" role="img" aria-label="Team member portrait placeholder"></div>
    <p class="member__name">James Smith</p><p class="member__role">Title</p>
    <div class="member__social"><span class="social--a"></span><span class="social--b"></span><span class="social--c"></span></div>
  </div>
  <div class="member" style="left:802px">
    <div class="member__portrait" role="img" aria-label="Team member portrait placeholder"></div>
    <p class="member__name">Mary LEE</p><p class="member__role">Title</p>
    <div class="member__social"><span class="social--a"></span><span class="social--b"></span><span class="social--c"></span></div>
  </div>

  <div class="brand"><span class="brand__dot"></span>Bellwether Ad Collective</div>
  <div class="domain">WWW.YOURDOMAIN.COM</div>
</section>

<section class="slide slide--contact">
  <div class="city-backdrop" role="img" aria-label="Evening view of a lakeside city with a bridge and hills, tinted blue"></div>
  <h2 class="contact__title">Contact Information</h2>

  <div class="contact-item">
    <svg class="contact-item__icon" style="left:64px;top:150px" width="44" height="56" viewBox="0 0 44 56" fill="none" stroke="#fff" stroke-width="2.5">
      <path d="M22 53 C10 38 3 29 3 20 A19 19 0 0 1 41 20 C41 29 34 38 22 53 Z"/><circle cx="22" cy="20" r="8"/>
    </svg>
    <span class="contact-item__label" style="left:128px;top:153px">Location</span>
    <div class="contact-item__panel" style="left:124px;top:182px;width:217px;line-height:1.38">ALDERBROOK OFFICE<br>Suite #512,<br>118-3340 Lakeview Ave<br>Alderbrook, MB, R3T 4K7</div>
  </div>

  <div class="contact-item">
    <svg class="contact-item__icon" style="left:388px;top:154px" width="34" height="64" viewBox="0 0 34 64" fill="none" stroke="#fff" stroke-width="2.5">
      <rect x="2" y="2" width="30" height="60" rx="4"/><line x1="2" y1="10" x2="32" y2="10"/><line x1="2" y1="52" x2="32" y2="52"/><line x1="13" y1="6" x2="21" y2="6"/>
    </svg>
    <span class="contact-item__label" style="left:444px;top:157px">Telephone</span>
    <div class="contact-item__panel panel--tight" style="left:440px;top:186px;width:223px">204.555.0142 (Tel)<br>204.555.0187 (Fax)<br>877.555.0163 (Toll Free)</div>
  </div>

  <div class="contact-item">
    <svg class="contact-item__icon" style="left:680px;top:160px" width="56" height="54" viewBox="0 0 56 54" fill="none" stroke="#fff" stroke-width="2.5">
      <circle cx="28" cy="27" r="25"/><ellipse cx="28" cy="27" rx="11" ry="25"/><line x1="3" y1="27" x2="53" y2="27"/><line x1="7" y1="15" x2="49" y2="15"/><line x1="7" y1="39" x2="49" y2="39"/><line x1="28" y1="2" x2="28" y2="52"/>
    </svg>
    <span class="contact-item__label" style="left:744px;top:161px">Website</span>
    <div class="contact-item__panel" style="left:744px;top:188px;width:227px;font-size:16px;line-height:1.3">www.foxglovepromotions.ca/</div>
  </div>

  <div class="contact-item">
    <svg class="contact-item__icon" style="left:288px;top:326px" width="46" height="38" viewBox="0 0 46 38" fill="none" stroke="#fff" stroke-width="2.5">
      <rect x="2" y="2" width="42" height="34"/><path d="M2 2 L23 22 L44 2"/><path d="M2 36 L18 18"/><path d="M44 36 L28 18"/>
    </svg>
    <span class="contact-item__label" style="left:354px;top:328px">Contact</span>
    <div class="contact-item__panel" style="left:346px;top:356px;width:375px;height:76px;line-height:1.5">Dale Thornbury<br>Sales &amp; Operations Manager<br>dale@foxglovepromotions.ca</div>
  </div>
</section>

</body>
</html>
```